Lomi Lomi Business
Zielgruppe
Lomi Lomi Massage /Wellnessmassage
Aufgabenstellung
Design, Farbgebung und Maße bitte angelehnt an das Velkaro-Design #22
Format 10,5x21cm Querformat (DIN Lang plus beim Anbieter "Prospektwelle" genannt)
Texte siehe Anhang
Daten bitte in editierbarem Illustrator, oder InDesign-Format

```html
<!DOCTYPE html>
<html lang="de">
<head>
<meta charset="utf-8">
<title>Lomi Lomi – Hawaiianische Massage &amp; Körperarbeit</title>
<link href="https://fonts.googleapis.com/css2?family=Play:wght@400;700&display=swap" rel="stylesheet">
<style>
  :root {
    --leaf-green: #5b8a0e;
    --sand: #fbd9a1;
    --slate: #575556;
    --paper: #ffffff;
    --ink-light: #f4f4f4;
  }
  * { margin: 0; padding: 0; box-sizing: border-box; }
  html, body { width: 1200px; height: 600px; overflow: hidden; background: var(--paper); }
  body { font-family: "Play", sans-serif; }
  .flyer { position: relative; width: 1200px; height: 600px; overflow: hidden; background: var(--paper); }

  .bamboo-visual {
    position: absolute; left: -20px; top: 300px; width: 640px; height: 320px;
    border-radius: 40% 60% 10% 10% / 45% 55% 10% 10%;
    background: radial-gradient(ellipse at 45% 40%, #8cc54a 0%, #6aa630 45%, #cfe6b4 85%, rgba(255,255,255,0) 100%);
  }
  .wave { position: absolute; inset: 0; width: 1200px; height: 600px; }

  .intro {
    position: absolute; left: 40px; top: 58px;
    color: var(--leaf-green); font-size: 17.6px; line-height: 21.7px; letter-spacing: 0.7px;
    white-space: nowrap;
  }
  .intro p + p { margin-top: 21.7px; }

  .contact {
    position: absolute; left: 830px; top: 47px;
    color: var(--ink-light); font-size: 17.6px; line-height: 20.4px; letter-spacing: 0.5px;
    white-space: nowrap;
  }
  .contact-title { color: var(--leaf-green); font-weight: 700; font-size: 17.6px; margin-bottom: 20px; }
  .contact-phone { margin-top: 20px; }
  .contact-hours { margin-top: 40px; }

  .portrait {
    position: absolute; left: 661px; top: 343px; width: 156px; height: 219px;
    border: 3px solid var(--sand);
    background: linear-gradient(160deg, #e6c88f 0%, #d9b479 50%, #2a2a2c 78%);
  }
  .bio {
    position: absolute; left: 830px; top: 459px;
    color: var(--sand); font-size: 17.6px; line-height: 20.2px; letter-spacing: 0.5px;
    white-space: nowrap;
  }
</style>
</head>
<body>
<main class="flyer">
  <div class="bamboo-visual" role="img" aria-label="Foto: grüner Bambuszweig mit Blättern"></div>

  <svg class="wave" viewBox="0 0 1200 600" aria-hidden="true">
    <path fill="var(--leaf-green)" d="M752 0 C800 80 790 200 705 305 C640 385 570 445 582 525 C587 560 598 585 606 600 L1200 600 L1200 0 Z"/>
    <path fill="var(--sand)" d="M762 0 C808 80 800 200 715 305 C650 385 586 445 598 525 C603 560 615 585 625 600 L1200 600 L1200 0 Z"/>
    <path fill="var(--slate)" d="M775 0 C822 80 812 200 728 305 C664 385 604 445 616 525 C621 560 633 585 643 600 L1200 600 L1200 0 Z"/>
  </svg>

  <section class="intro">
    <p>Die hawaiianische Lomi Lomi Massage (oder Tempelmassage) ist eine<br>
      Berührungskunst, welche von den Kahunas – den Wissensträgern – bis heute<br>
      praktiziert und weitergegeben wird. In der Massage wird der gesamte Körper unter<br>
      Verwendung von hochwertigem Massageöl mit Handballen und Unterarmen in<br>
      langen, fließenden Bewegungen massiert und ausgestrichen. Dadurch kann die<br>
      Behandlung&nbsp; zu einer tiefen Entspannung führen und Stress abbauen.</p>
    <p>Die Intensität und den Charakter der Massage bestimmen dabei<br>
      der Körper des Klienten und das Wesen des Moments.<br>
      Der Intimbereich bleibt dabei stets abgedeckt und unberührt.</p>
  </section>

  <section class="contact">
    <h2 class="contact-title">Kontakt:</h2>
    <p>Jonas Verhalen<br>
      Hawaiianische Massage &amp; Körperarbeit<br>
      Lindenhofgasse 7, 96052 Talbrunn<br>
      ( Eingang „Die Feinwerkstatt“)</p>
    <p class="contact-phone">Telefon&nbsp; 0931-480 372 56</p>
    <p class="contact-hours">Termine nach Vereinbarung</p>
  </section>

  <div class="portrait" role="img" aria-label="Porträtfoto des Masseurs"></div>

  <section class="bio">
    <p>Jonas Verhalen – Jahrgang 1979<br>
      Lomi Lomi Practitioner<br>
      (nach Kahu Nalani von Maunaloa)<br>
      Romi-Kahuna-Bodywork Practitioner<br>
      Wellnessmasseur &amp; Wellnesstherapeut</p>
  </section>
</main>
</body>
</html>
```